Charity Initiative needs a WebPage design

We need a web design for charity initiative by two young guys riding their bikes around Australia to support KestrelWay which helps people with depression and anxiety. Full brief and requirements are attached in the PDF and word document. We have the logo already done and attached. Website will be done in Wordpress and need to get Donations, display current donations, show live Video feed, GPS tracker, Blogs etc and also ability to sell merchandise later

Target Market(s)

Sponsors, Business, Young People

Number of Pages Required

4 page

Font styles to use
Serif
Sans Serif
Decorative
Script

Requirements
Must have
• As per Brief and also Donation status etc
Nice to have
• Please check my logo and read the Bried

```html
<!DOCTYPE html>
<html lang="en">
<head>
<meta charset="utf-8">
<title>Long Road Ride – Charity Ride</title>
<link href="https://fonts.googleapis.com/css2?family=Raleway:wght@500;600;700;800&family=Open+Sans:ital,wght@0,400;0,600;0,700;1,400&display=swap" rel="stylesheet">
<style>
:root{
  --pink:#ec2a6c;
  --teal:#3bb6b1;
  --teal-dark:#2a9e9a;
  --yellow:#f1b31c;
  --ink:#2d2d2d;
  --text:#6b6b6b;
  --light:#f4f5f5;
  --dark:#1f2121;
  --backdrop:#f8dedd;
}
*{box-sizing:border-box;margin:0;padding:0}
html,body{width:1200px;height:2267px;overflow:hidden}
body{background:var(--backdrop);font-family:"Open Sans",Arial,sans-serif;color:var(--text);position:relative}
.page{position:absolute;left:162px;top:0;width:876px;height:2267px;background:#fff;overflow:hidden}
.top-strip{height:4px;background:linear-gradient(90deg,var(--teal),var(--pink),var(--yellow),var(--teal))}
h2{font-family:"Raleway",sans-serif;font-weight:700;color:var(--ink);font-size:24px;line-height:28px;letter-spacing:.3px}
.btn{position:absolute;display:flex;align-items:center;justify-content:center;border-radius:20px;font-family:"Raleway",sans-serif;font-weight:700;font-size:11px;text-transform:uppercase;color:#fff;background:var(--pink);white-space:nowrap}

/* header */
.site-header{position:relative;height:102px;background:#f7f7f7}
.brand{position:absolute;left:20px;top:30px;display:flex;align-items:center;gap:8px;font-family:"Raleway",sans-serif;font-weight:800;font-size:22px;color:var(--pink)}
.brand .dot{width:18px;height:18px;border-radius:50%;background:var(--pink)}
.nav{position:absolute;top:46px;left:0;font-family:"Raleway",sans-serif;font-weight:700;font-size:11px;color:#333}
.nav span{position:absolute;white-space:nowrap}
.nav .active{color:var(--teal)}
.nav-search{position:absolute;left:683px;top:45px}
.btn-donate-top{left:741px;top:36px;width:114px;height:33px}

/* hero */
.hero{position:relative;height:388px;background:linear-gradient(160deg,#6f7e62 0%,#4d5a47 35%,#3b3f3d 60%,#6c6f6d 100%)}
.hero-edge{position:absolute;top:-6px;left:0;width:876px;height:18px}
.hero-caption{position:absolute;left:544px;top:103px;width:320px;text-align:center;color:#fff}
.hero-caption .kicker{font-family:"Raleway",sans-serif;font-weight:500;font-size:18px;line-height:22px}
.hero-caption .title{font-family:"Raleway",sans-serif;font-weight:800;font-size:27px;line-height:34px;margin-top:4px;white-space:nowrap}
.hero-caption p{font-size:12px;line-height:19px;margin:6px auto 0;width:270px}
.dots{position:absolute;left:680px;top:253px;display:flex;gap:9px}
.dots i{width:14px;height:14px;border-radius:50%;border:2px solid #fff}
.dots i.on{background:var(--pink)}

/* welcome */
.welcome{position:relative;height:330px}
.video{position:absolute;left:20px;top:39px;width:375px;height:245px;border:1px solid #e2e2e2;background:#f8f8f8}
.video-art{position:absolute;left:30px;top:30px;width:315px;height:130px;background:linear-gradient(90deg,#f6c0d3,#d9d4cf 55%,#bfe6e3)}
.video-bar{position:absolute;left:10px;right:10px;bottom:12px;height:28px;display:flex;gap:6px}
.video-bar .play{width:48px;background:#3a3a3a;display:flex;align-items:center;justify-content:center}
.video-bar .track{flex:1;background:#2f2f2f;position:relative}
.video-bar .track::before{content:"";position:absolute;left:6px;top:11px;width:210px;height:5px;background:#555}
.video-bar .track::after{content:"";position:absolute;left:6px;top:11px;width:78px;height:5px;background:#2d8fd5}
.welcome-text{position:absolute;left:433px;top:42px;width:425px}
.welcome-text h2 span{color:var(--teal)}
.welcome-text p{font-size:10.5px;line-height:20px;margin-top:10px}
.btn-welcome{left:433px;top:250px;width:114px;height:34px}

/* tracking */
.tracking{position:relative;height:420px;background:linear-gradient(135deg,#3dbab4,#2aa7a2 60%,#33b1ab)}
.tracking h2{position:absolute;left:20px;top:42px;color:#fff}
.track-item{position:absolute;left:20px;display:flex;gap:20px;color:#fff}
.pin{width:36px;height:36px;border:2px solid #fff;border-radius:50%;display:flex;align-items:center;justify-content:center;flex:none}
.track-item p{font-size:10px;font-style:italic;margin-top:3px}
.track-item .time{font-size:10px;font-weight:700;margin-top:10px;display:flex;align-items:center;gap:6px}
.btn-track{left:20px;top:327px;width:116px;height:35px}
.btn-view{left:147px;top:327px;width:115px;height:35px;background:#f1f1f1;color:var(--pink)}
.device{position:absolute;left:591px;top:23px;width:190px;height:300px;border-radius:24px;background:linear-gradient(160deg,#f1f1f1,#d8dcdc 50%,#e8c9b8)}

/* donation */
.donation{position:relative;height:385px}
.donation h2{position:absolute;left:20px;top:40px}
.donation>p{position:absolute;left:20px;top:78px;width:720px;font-size:11px;line-height:20px}
.progress{position:absolute;left:26px;top:143px;width:828px;height:30px;border-radius:15px;background:#fff;border:2px solid #eee}
.progress .fill{position:absolute;left:8px;top:6px;width:377px;height:14px;border-radius:7px;background:repeating-linear-gradient(120deg,var(--pink) 0 14px,#f04f86 14px 20px)}
.knob{position:absolute;top:143px;width:33px;height:33px;border-radius:50%;border:4px solid #fff;box-shadow:0 0 0 2px #eee}
.tick{position:absolute;top:178px;width:2px;height:40px;background:#ddd}
.tick::after{content:"";position:absolute;left:-3px;bottom:-4px;width:8px;height:8px;border-radius:50%;background:#ddd}
.fund{position:absolute;top:244px;font-family:"Raleway",sans-serif;font-weight:600;font-size:11px;text-transform:uppercase;white-space:nowrap}
.fund b{display:block;font-size:11px;margin-top:6px;text-align:center}
.btn-donate{left:21px;top:298px;width:192px;height:42px;border-radius:22px}
.current{position:absolute;left:225px;top:298px;width:629px;height:42px;border-radius:22px;border:2px solid #eee;display:flex;align-items:center;overflow:hidden}
.current .label{width:192px;height:42px;background:var(--yellow);color:#fff;font-family:"Raleway",sans-serif;font-weight:700;font-size:11px;display:flex;align-items:center;justify-content:center;clip-path:polygon(0 0,92% 0,100% 50%,92% 100%,0 100%)}
.current .amount{flex:1;text-align:center;font-weight:600;font-size:11px;color:#333;border-left:1px solid #e3e3e3}
.current .amount:first-of-type{border-left:0}

/* journal */
.journal{position:relative;height:408px;background:var(--light)}
.journal h2{position:absolute;left:20px;top:40px}
.post{position:absolute;left:21px;width:544px;height:127px;background:#fff;border:1px solid #e6e6e6}
.post .thumb{position:absolute;left:5px;top:4px;width:180px;height:118px}
.post h3{position:absolute;left:215px;top:20px;font-family:"Open Sans",sans-serif;font-weight:600;font-size:12px;color:var(--teal)}
.post p{position:absolute;left:215px;top:44px;width:310px;font-size:10px;font-style:italic;line-height:19px;color:#555}
.post .meta{position:absolute;left:215px;top:92px;font-size:8px;font-style:italic;color:var(--teal);display:flex;gap:14px}
.partner{position:absolute;left:591px;top:44px;width:266px;height:319px;background:#fff;border:1px solid #e6e6e6}
.partner-head{height:44px;background:var(--teal);color:#fff;font-family:"Raleway",sans-serif;font-weight:600;font-size:19px;display:flex;align-items:center;justify-content:space-between;padding:0 18px}
.partner-art{margin:14px auto 0;width:200px;height:120px;background:linear-gradient(90deg,#f2a9c3,#f6d48a 50%,#d6dcec)}
.partner p{font-size:10px;line-height:19px;padding:10px 18px 0}
.partner a{display:block;padding:6px 18px;font-size:10px;color:var(--pink);text-decoration:underline}

/* footer */
.site-footer{position:relative;height:180px;background:var(--dark);color:#bbb}
.footer-brand{position:absolute;left:20px;top:60px;display:flex;align-items:center;gap:10px;font-family:"Raleway",sans-serif;font-weight:800;font-size:26px;color:#9a9a9a}
.footer-brand .dot{width:20px;height:20px;border-radius:50%;background:#9a9a9a}
.site-footer h4{font-family:"Raleway",sans-serif;font-weight:700;font-size:12px;color:#fff;margin-bottom:14px}
.fcol{position:absolute;top:28px;font-size:10px}
.menu li{list-style:none;line-height:21px}
.menu li::before{content:"›";margin-right:7px}
.newsletter p{width:190px;line-height:20px}
.subscribe{margin-top:12px;display:flex;width:218px;height:32px;border-radius:16px;overflow:hidden}
.subscribe span{flex:1;background:#fff;color:#999;padding-left:16px;display:flex;align-items:center;font-size:10px}
.subscribe b{width:72px;background:var(--pink);color:#fff;font-size:9px;display:flex;align-items:center;justify-content:center}
.contact li{list-style:none;display:flex;gap:10px;line-height:19px;margin-bottom:8px}
.contact svg{flex:none;margin-top:4px}
.bottom-bar{position:relative;height:50px;background:var(--teal);color:#fff;font-size:10px}
.bottom-bar .copy{position:absolute;left:20px;top:19px}
.social{position:absolute;left:622px;top:12px;display:flex;align-items:center;gap:6px}
.social span{margin-right:4px}
.social i{width:24px;height:24px;border-radius:50%;border:2px solid #fff}
</style>
</head>
<body>
<div class="page">
  <div class="top-strip"></div>

  <header class="site-header">
    <div class="brand"><span class="dot"></span>Long Road Ride</div>
    <nav class="nav">
      <span class="active" style="left:357px">HOME</span>
      <span style="left:431px">BLOG</span>
      <span style="left:516px">PROGRESS</span>
      <span style="left:613px">CONTACT</span>
    </nav>
    <svg class="nav-search" width="12" height="12" viewBox="0 0 12 12"><circle cx="5" cy="5" r="3.5" fill="none" stroke="#3bb6b1" stroke-width="1.8"/><line x1="7.6" y1="7.6" x2="11" y2="11" stroke="#3bb6b1" stroke-width="1.8"/></svg>
    <div class="btn btn-donate-top">Donate Now!</div>
  </header>

  <section class="hero" role="img" aria-label="Group of motorcycle riders on a city road">
    <svg class="hero-edge" viewBox="0 0 876 18" preserveAspectRatio="none"><path d="M0 0H876V8L850 12 820 6 790 13 760 7 720 12 690 5 650 11 610 6 580 13 540 7 500 12 470 5 430 12 400 6 360 13 320 7 290 12 250 5 210 11 180 6 140 13 100 7 70 12 40 6 0 11Z" fill="#f7f7f7"/></svg>
    <div class="hero-caption">
      <div class="kicker">BIKE RIDES TO</div>
      <div class="title">CHARITY DONATIONS</div>
      <p>Neque porro quisquam est, qui doloremsa ipsum quia dolor sit amet, consectetuer, adipisci velit, sed quia non...</p>
    </div>
    <div class="dots"><i class="on"></i><i></i><i></i></div>
  </section>

  <section class="welcome">
    <div class="video">
      <div class="video-art" role="img" aria-label="Ride emblem shown as video poster"></div>
      <div class="video-bar">
        <div class="play"><svg width="12" height="12" viewBox="0 0 12 12"><path d="M2 1L11 6 2 11Z" fill="#fff"/></svg></div>
        <div class="track"></div>
      </div>
    </div>
    <div class="welcome-text">
      <h2>WELCOME TO <span>LONG ROAD RIDE</span></h2>
      <p>Nemo enim ipsam voluptatem quia voluptas sit aspernatur aut odit aut fugit, sed quia consequuntur magni dolores eos qui ratione voluptatem sequi nesciunt. Neque porro quisquam est, qui dolorem ipsum quia dolor sit amet, consectetur, adipisci velit, sed quia non numquam ipsum...</p>
      <p>Consequuntur magni dolores eos qui ratione voluptatem sequi nesciunt. Neque porro quisquam est, qui dolorem ipsum quia dolor sit amet, consectetur, adipisci velit, sed quia non numquam ipsum...</p>
    </div>
    <div class="btn btn-welcome">Click Here</div>
  </section>

  <section class="tracking">
    <h2>TRACKING OUR BIKES</h2>
    <div class="track-item" style="top:114px">
      <div class="pin"><svg width="14" height="18" viewBox="0 0 14 18"><path d="M7 1a6 6 0 0 1 6 6c0 4-6 10-6 10S1 11 1 7a6 6 0 0 1 6-6z" fill="none" stroke="#fff" stroke-width="1.6"/><circle cx="7" cy="7" r="2" fill="#fff"/></svg></div>
      <div><p>Nemo enim ipsam voluptatem quia voluptas sit aspernatur aut odit aut fugit, sed quia...</p><div class="time"><svg width="10" height="10" viewBox="0 0 10 10"><circle cx="5" cy="5" r="4" fill="none" stroke="#fff" stroke-width="1.4"/><path d="M5 2.5V5H7" fill="none" stroke="#fff" stroke-width="1.2"/></svg>TIME : 12:45 P.M</div></div>
    </div>
    <div class="track-item" style="top:188px">
      <div class="pin"><svg width="14" height="18" viewBox="0 0 14 18"><path d="M7 1a6 6 0 0 1 6 6c0 4-6 10-6 10S1 11 1 7a6 6 0 0 1 6-6z" fill="none" stroke="#fff" stroke-width="1.6"/><circle cx="7" cy="7" r="2" fill="#fff"/></svg></div>
      <div><p>Nemo enim ipsam voluptatem quia voluptas sit aspernatur aut odit aut fugit, sed quia...</p><div class="time"><svg width="10" height="10" viewBox="0 0 10 10"><circle cx="5" cy="5" r="4" fill="none" stroke="#fff" stroke-width="1.4"/><path d="M5 2.5V5H7" fill="none" stroke="#fff" stroke-width="1.2"/></svg>TIME : 12:45 P.M</div></div>
    </div>
    <div class="track-item" style="top:262px">
      <div class="pin"><svg width="14" height="18" viewBox="0 0 14 18"><path d="M7 1a6 6 0 0 1 6 6c0 4-6 10-6 10S1 11 1 7a6 6 0 0 1 6-6z" fill="none" stroke="#fff" stroke-width="1.6"/><circle cx="7" cy="7" r="2" fill="#fff"/></svg></div>
      <div><p>Nemo enim ipsam voluptatem quia voluptas sit aspernatur aut odit aut fugit, sed quia...</p><div class="time"><svg width="10" height="10" viewBox="0 0 10 10"><circle cx="5" cy="5" r="4" fill="none" stroke="#fff" stroke-width="1.4"/><path d="M5 2.5V5H7" fill="none" stroke="#fff" stroke-width="1.2"/></svg>TIME : 12:45 P.M</div></div>
    </div>
    <div class="btn btn-track">Click Here</div>
    <div class="btn btn-view">View Ride</div>
    <div class="device" role="img" aria-label="Hand holding a phone showing the live GPS route map"></div>
  </section>

  <section class="donation">
    <h2>DONATION TARGET</h2>
    <p>Nemo enim ipsam voluptatem quia voluptas sit aspernatur aut odit aut fugit, sed quia consequuntur magni dolores eos qui ratione voluptatem incidunt ut labore et dolore magnam aliquam quaerat voluptatem. Ut enim...</p>
    <div class="progress"><div class="fill"></div></div>
    <div class="knob" style="left:47px;background:var(--pink)"></div>
    <div class="knob" style="left:420px;background:var(--yellow)"></div>
    <div class="knob" style="left:804px;background:var(--teal)"></div>
    <div class="tick" style="left:63px"></div>
    <div class="tick" style="left:436px"></div>
    <div class="tick" style="left:820px"></div>
    <div class="fund" style="left:21px;color:var(--pink)">Starting Fund<b>$1.00</b></div>
    <div class="fund" style="left:396px;color:var(--yellow)">Average Fund<b>$200.00</b></div>
    <div class="fund" style="left:786px;color:var(--teal)">Our Target<b>$500.00</b></div>
    <div class="btn btn-donate">Donate Now Click Here</div>
    <div class="current">
      <div class="label">CURRENT DONATIONS</div>
      <div class="amount">$6865. 000</div>
      <div class="amount">$6865. 000</div>
      <div class="amount">$6865. 000</div>
      <div class="amount">$6865. 000</div>
    </div>
  </section>

  <section class="journal">
    <h2>RECENT JOURNAL</h2>
    <article class="post" style="top:93px">
      <div class="thumb" role="img" aria-label="Rider on a motorcycle at sunset" style="background:linear-gradient(135deg,#e8b04a,#b07a3a 55%,#5b5044)"></div>
      <h3>Jordan Hale</h3>
      <p>"Neque porro quisquam est, qui dolorem ipsum quia dolor sit am tempora incidunt ut labore et dolore magnam aliquam quaerat"</p>
      <div class="meta"><span>June 23 2016</span><span>Leave a Comments</span></div>
    </article>
    <article class="post" style="top:235px">
      <div class="thumb" role="img" aria-label="Motorcycle handlebars on an open road at sunrise" style="background:linear-gradient(135deg,#f3c670,#9a7a4e 50%,#3d3a33)"></div>
      <h3>Jordan Hale</h3>
      <p>"Neque porro quisquam est, qui dolorem ipsum quia dolor sit am tempora incidunt ut labore et dolore magnam aliquam quaerat"</p>
      <div class="meta"><span>June 23 2016</span><span>Leave a Comments</span></div>
    </article>
    <aside class="partner">
      <div class="partner-head">KestrelWay<svg width="14" height="14" viewBox="0 0 14 14"><circle cx="7" cy="7" r="7" fill="#fff"/><path d="M7 3.5V10.5M3.5 7H10.5" stroke="#3bb6b1" stroke-width="2"/></svg></div>
      <div class="partner-art" role="img" aria-label="Supported charity artwork"></div>
      <p>Duis mollis, est non commodo luctus, nisi erat porttitor ligula, eget lacinia odio sem nec elit. Cras mattis consectetur purus sit amet fermentum. Fusce dapibus, tellus ac cur...</p>
      <a>Click View More Information!</a>
    </aside>
  </section>

  <footer class="site-footer">
    <div class="footer-brand"><span class="dot"></span>Long Road Ride</div>
    <div class="fcol" style="left:313px">
      <h4>MENU</h4>
      <ul class="menu"><li>Home</li><li>Blog</li><li>Progress</li><li>Contact</li><li>Donate</li></ul>
    </div>
    <div class="fcol newsletter" style="left:416px">
      <h4>NEWSLETTER</h4>
      <p>Incidunt ut labore et dolore magnam aliquam quaerat voluptatem...</p>
      <div class="subscribe"><span>Enter e-mail</span><b>SUBSCRIBE</b></div>
    </div>
    <div class="fcol" style="left:682px;width:180px">
      <h4>CONTACT INFO</h4>
      <ul class="contact">
        <li><svg width="9" height="12" viewBox="0 0 14 18"><path d="M7 1a6 6 0 0 1 6 6c0 4-6 10-6 10S1 11 1 7a6 6 0 0 1 6-6z" fill="#ec2a6c"/></svg>27 Harbour Lane, Westfield-3190</li>
        <li><svg width="10" height="10" viewBox="0 0 10 10"><path d="M2 0.5L4 3 3 4.5C3.8 6 4.5 6.6 5.5 7L7 6 9.5 8 8.5 9.5C4.5 9.5 0.5 5.5 0.5 1.5Z" fill="#ec2a6c"/></svg>Phone : (+100) 555-0142</li>
        <li><svg width="11" height="9" viewBox="0 0 11 9"><rect width="11" height="9" rx="1" fill="#ec2a6c"/><path d="M1 1.5L5.5 5 10 1.5" fill="none" stroke="#1f2121" stroke-width="1"/></svg>Mail : info@longroadride.com</li>
      </ul>
    </div>
  </footer>

  <div class="bottom-bar">
    <div class="copy">Copyrights©longroadride.2016 | Allrights Reserved.</div>
    <div class="social"><span>Connect With Us :</span><i></i><i></i><i></i><i></i><i></i></div>
  </div>
</div>
</body>
</html>
```